Ads for Law Firm

I am an employment lawyer who represents individual employees. I currently have a banner ad on sites focused on individual employment rights, like StaffLedgerHub.org and TallpineGuidance.com. I am looking for an ad that incorporates best practices for promoting a professional service.

I am attaching a couple of existing ads that I want to replace. The new ad should be the same dimension as the attached. The old ad is a friend helped with, and focuses on my great credentials.

I have read that people looking for lawyers care a less about credentials, and more about whether the lawyer can protect them. It should also have a call to action, being to call or email me. Therefore, the ad should say something like "call [me/Toby] to protect your [job/employment/rights/etc],"

Lawyer

```html
<!DOCTYPE html>
<html lang="en">
<head>
<meta charset="utf-8">
<title>Law Firm Banner</title>
<link rel="stylesheet" href="https://fonts.googleapis.com/css2?family=Open+Sans:wght@400;600&display=swap">
<style>
  :root {
    --page-bg: #ffffff;
    --accent-green: #6b9b35;
    --ink: #111111;
    --navy: #0e3450;
    --navy-deep: #0a2a42;
    --sky-line: #a9c9da;
    --crimson: #c4113c;
    --panel-light: #f3f5f7;
    --panel-mid: #e4e8ec;
    --photo-tone-a: #c9cfd6;
    --photo-tone-b: #8d97a3;
  }
  * { margin: 0; padding: 0; box-sizing: border-box; }
  html, body {
    width: 1200px; height: 549px; overflow: hidden;
    background: var(--page-bg);
    font-family: "Open Sans", Arial, sans-serif;
    color: var(--ink);
  }
  .board { position: relative; width: 1200px; height: 549px; }
  .top-rule {
    position: absolute; left: 0; top: 0; width: 100%; height: 9px;
    background: var(--accent-green);
  }
  .board-title {
    position: absolute; left: 0; width: 1192px; top: 14px;
    text-align: center; font-size: 25px; font-weight: 400;
  }
  .banner-frame {
    position: absolute; left: 229px; top: 210px;
    width: 734px; height: 94px;
  }
  .banner {
    position: relative; width: 468px; height: 60px; overflow: hidden;
    transform: scale(1.5684); transform-origin: 0 0;
    background: linear-gradient(90deg, #ffffff 0%, var(--panel-light) 55%, var(--panel-mid) 100%);
    border: 1px solid var(--navy-deep);
  }
  .banner-curve { position: absolute; left: 0; top: 0; width: 468px; height: 60px; }
  .monogram {
    position: absolute; left: 9px; top: 12px;
    font-size: 24px; font-weight: 400; color: #ffffff; letter-spacing: 1px;
  }
  .lawyer-name {
    position: absolute; left: 160px; width: 240px; top: 0px;
    text-align: center; font-size: 16px; color: var(--navy);
  }
  .lawyer-role {
    position: absolute; left: 140px; width: 280px; top: 20px;
    text-align: center; font-size: 13.5px; color: var(--crimson);
  }
  .call-button {
    position: absolute; left: 78px; top: 40px; width: 52px; height: 18px;
    background: var(--navy); color: #ffffff; border-radius: 4px;
    font-size: 11.5px; line-height: 18px; text-align: center;
  }
  .promise {
    position: absolute; left: 141px; top: 42px;
    font-size: 11.5px; line-height: 15px; color: var(--ink);
    display: flex; align-items: center; white-space: nowrap;
  }
  .promise .benefit { display: inline-flex; align-items: center; margin-left: 5px; }
  .promise .tick { width: 8px; height: 8px; margin-right: 1px; }
  .portrait {
    position: absolute; right: 0; top: 0; width: 64px; height: 58px;
    background: linear-gradient(180deg, var(--photo-tone-a) 0%, var(--photo-tone-b) 100%);
  }
  .size-caption {
    position: absolute; left: 0; width: 1224px; top: 334px;
    text-align: center; font-size: 19px;
  }
</style>
</head>
<body>
  <main class="board">
    <div class="top-rule"></div>
    <h1 class="board-title">Law Firm Banner</h1>

    <div class="banner-frame">
      <div class="banner">
        <svg class="banner-curve" viewBox="0 0 468 60" aria-hidden="true">
          <path d="M0 0 H96 Q70 28 74 60 H0 Z" fill="var(--navy)"/>
          <path d="M96 0 Q70 28 74 60" fill="none" stroke="var(--sky-line)" stroke-width="3"/>
          <path d="M104 0 Q80 26 84 60" fill="none" stroke="#dfe9ef" stroke-width="2"/>
        </svg>
        <div class="monogram">TH</div>
        <div class="lawyer-name">Toby Halvorsen</div>
        <div class="lawyer-role">Ohio Employment Law Specialist</div>
        <div class="call-button">Call Toby</div>
        <div class="promise">
          <span>to protect your</span>
          <span class="benefit">
            <svg class="tick" viewBox="0 0 8 8" aria-hidden="true"><path d="M1 4.5 L3 6.5 L7 1.5" fill="none" stroke="var(--navy)" stroke-width="1.6"/></svg>Job
          </span>
          <span class="benefit">
            <svg class="tick" viewBox="0 0 8 8" aria-hidden="true"><path d="M1 4.5 L3 6.5 L7 1.5" fill="none" stroke="var(--navy)" stroke-width="1.6"/></svg>Rights
          </span>
          <span class="benefit">
            <svg class="tick" viewBox="0 0 8 8" aria-hidden="true"><path d="M1 4.5 L3 6.5 L7 1.5" fill="none" stroke="var(--navy)" stroke-width="1.6"/></svg>Employment
          </span>
        </div>
        <div class="portrait" role="img" aria-label="Portrait photo of the lawyer in a suit and tie"></div>
      </div>
    </div>

    <p class="size-caption">468 x 60</p>
  </main>
</body>
</html>
```